Business Cards for Communications Technology Company

We are an innovative software company based in Tropical North Queensland, Australia. We have several brands with a focus on communications software for businesses. We are looking for a business card that is very innovate and creative whilst still remaining professional on a corporate level.

Our internal culture is very progressive and expresses a blend between the clarity of our natural surroundings and the highly technological industry we work in. Our current branding blends a modern minimalist typeface with the desire to push the boundaries in the way we communicate.

This is a corporate level business card for the communications software industry and may possibly also encompass our brands PelNetwork, PelCopy, PelPost and our B2B marketing service—with our companies name being Tarvix Holdings. Showing other brands on the business card is optional not compulsory.

Technical notes:

-We will attach all logo's and some examples of our corporate branding
- Would be willing to print with various papers, embossed, metallic ink, curved edges etc. in a standard business card size

Sample content:

Dorian Malcott
Senior Account Manager
Phone: 1300 482 916 / +617 4385 2604
Email: d.malcott@tarvix.com.au
Web: www.tarvix.com.au

Sincerely,
Tarvix Holdings.

```html
<!DOCTYPE html>
<html lang="en">
<head>
<meta charset="utf-8">
<title>Tarvix Holdings – Business Card</title>
<link rel="stylesheet" href="https://fonts.googleapis.com/css2?family=Roboto:wght@300;400&display=swap">
<style>
  :root {
    --backdrop: #2b2b2d;
    --card-light: #f7f7f7;
    --card-dark: #252627;
    --ink-grey: #5a5c5f;
    --ink-soft: #6f7174;
    --ink-white: #f2f2f2;
    --accent-green: #6fa63a;
    --divider: #8a8c8f;
  }
  * { box-sizing: border-box; margin: 0; padding: 0; }
  html, body {
    width: 1200px;
    height: 900px;
    overflow: hidden;
    background: var(--backdrop);
    font-family: "Roboto", Arial, sans-serif;
  }
  .canvas {
    width: 1200px;
    height: 900px;
    display: flex;
    flex-direction: column;
    align-items: center;
    justify-content: center;
    gap: 40px;
  }
  .card {
    width: 600px;
    height: 367px;
    border-radius: 3px;
    position: relative;
    box-shadow: 0 6px 18px rgba(0,0,0,0.45);
  }
  .card--front {
    background: var(--card-light);
    display: flex;
    flex-direction: column;
    align-items: center;
    justify-content: center;
  }
  .brand {
    display: flex;
    align-items: center;
    gap: 14px;
    margin-top: -10px;
  }
  .brand__dot {
    width: 46px;
    height: 46px;
    border-radius: 50%;
    background: var(--ink-grey);
  }
  .brand__name {
    font-weight: 400;
    font-size: 44px;
    color: var(--ink-grey);
    letter-spacing: 1px;
  }
  .front-web {
    margin-top: 44px;
    font-weight: 300;
    font-size: 14px;
    letter-spacing: 8px;
    color: var(--ink-soft);
  }
  .card--back {
    background: var(--card-dark);
    display: flex;
    align-items: center;
    justify-content: center;
  }
  .identity {
    text-align: right;
    padding-right: 22px;
  }
  .identity__name {
    font-weight: 300;
    font-size: 27px;
    color: var(--accent-green);
    letter-spacing: 0.5px;
  }
  .identity__role {
    font-weight: 400;
    font-size: 16px;
    color: var(--ink-white);
    margin-top: 2px;
  }
  .divider {
    width: 2px;
    height: 96px;
    background: linear-gradient(to bottom, transparent, var(--divider), transparent);
  }
  .contacts {
    list-style: none;
    padding-left: 22px;
  }
  .contacts__item {
    display: flex;
    align-items: center;
    gap: 10px;
    font-size: 15.5px;
    color: var(--ink-white);
    line-height: 22px;
  }
  .contacts__icon {
    width: 14px;
    height: 14px;
    fill: var(--accent-green);
    flex: none;
  }
</style>
</head>
<body>
<main class="canvas">
  <section class="card card--front">
    <div class="brand">
      <span class="brand__dot"></span>
      <span class="brand__name">Tarvix Holdings</span>
    </div>
    <p class="front-web">www.tarvix.com.au</p>
  </section>

  <section class="card card--back">
    <div class="identity">
      <h1 class="identity__name">DORIAN MALCOTT</h1>
      <p class="identity__role">Senior Account Manager</p>
    </div>
    <div class="divider"></div>
    <ul class="contacts">
      <li class="contacts__item">
        <svg class="contacts__icon" viewBox="0 0 24 24"><path d="M6.6 10.8a15.1 15.1 0 0 0 6.6 6.6l2.2-2.2a1 1 0 0 1 1-.25 11.4 11.4 0 0 0 3.6.57 1 1 0 0 1 1 1V20a1 1 0 0 1-1 1A17 17 0 0 1 3 4a1 1 0 0 1 1-1h3.5a1 1 0 0 1 1 1c0 1.25.2 2.45.57 3.57a1 1 0 0 1-.25 1z"/></svg>
        1300 482 916
      </li>
      <li class="contacts__item">
        <svg class="contacts__icon" viewBox="0 0 24 24"><path d="M6.6 10.8a15.1 15.1 0 0 0 6.6 6.6l2.2-2.2a1 1 0 0 1 1-.25 11.4 11.4 0 0 0 3.6.57 1 1 0 0 1 1 1V20a1 1 0 0 1-1 1A17 17 0 0 1 3 4a1 1 0 0 1 1-1h3.5a1 1 0 0 1 1 1c0 1.25.2 2.45.57 3.57a1 1 0 0 1-.25 1z"/></svg>
        +617 4385 2604
      </li>
      <li class="contacts__item">
        <svg class="contacts__icon" viewBox="0 0 24 24"><path d="M2 5h20v14H2z M2 5l10 8 10-8" fill="var(--accent-green)"/><path d="M3 6l9 7 9-7" fill="none" stroke="var(--card-dark)" stroke-width="1.6"/></svg>
        d.malcott@tarvix.com.au
      </li>
      <li class="contacts__item">
        <svg class="contacts__icon" viewBox="0 0 24 24"><circle cx="12" cy="12" r="10"/><path d="M2 12h20M12 2c3 3 3 17 0 20M12 2c-3 3-3 17 0 20" fill="none" stroke="var(--card-dark)" stroke-width="1.5"/></svg>
        www.tarvix.com.au
      </li>
    </ul>
  </section>
</main>
</body>
</html>
```